Pool business needs attractive flyer

I just started my own pool service business, Here is the Information I want on the flyer but you put it anyway you think best.

Service Call $45
which Includes: Chemical Balance, Inspect all equipment, Skim water surface, clean filters.

Vacuum $10
Please Call, txt or Email for chemical price list

Other Services Include:
Supply and install Pumps, Chlorinators, Automatic Cleaners & Spare Parts

My Name
0417283951
TideDesk@quellmail.com

Pool Service

```html
<!DOCTYPE html>
<html lang="en">
<head>
<meta charset="utf-8">
<title>Bluecrest Pool Services – Flyer</title>
<link rel="stylesheet" href="https://fonts.googleapis.com/css2?family=Bangers&family=Arimo:ital,wght@0,400;0,700;1,400&display=swap">
<style>
  :root {
    --page-bg: #e9ecef;
    --pool-deep: #1f5f9e;
    --pool-mid: #3f8fd0;
    --pool-light: #9fd0f0;
    --pool-shade: #2c4f6e;
    --stone: #b79a78;
    --navy: #22457f;
    --navy-dark: #15305e;
    --accent-blue: #3b86cf;
    --band-blue: #5b9ad6;
    --panel-grey: #c9ced4;
    --text-dark: #2b2b2b;
    --white: #ffffff;
  }
  * { box-sizing: border-box; margin: 0; padding: 0; }
  html, body { width: 1200px; height: 1000px; overflow: hidden; }
  body {
    background: var(--page-bg);
    font-family: "Arimo", Arial, sans-serif;
    position: relative;
  }
  .flyer {
    position: absolute;
    left: 300px; top: 50px;
    width: 600px; height: 900px;
    background: var(--white);
    overflow: hidden;
    box-shadow: 0 6px 24px rgba(0,0,0,.18);
  }
  .hero-photo {
    position: absolute; left: 0; top: 0;
    width: 600px; height: 480px;
    background:
      radial-gradient(ellipse 220px 140px at 250px 300px, rgba(235,205,175,.75), rgba(235,205,175,0) 70%),
      radial-gradient(ellipse 200px 90px at 170px 430px, rgba(183,154,120,.85), rgba(183,154,120,0) 75%),
      radial-gradient(ellipse 180px 120px at 470px 230px, rgba(225,240,252,.7), rgba(225,240,252,0) 70%),
      linear-gradient(100deg, var(--pool-light) 0%, var(--pool-mid) 35%, var(--pool-deep) 65%, var(--pool-shade) 100%);
  }
  .brand {
    position: absolute; left: 0; top: 60px; width: 600px;
    display: flex; justify-content: center; align-items: center; gap: 14px;
  }
  .brand-dot {
    width: 44px; height: 44px; border-radius: 50%;
    background: var(--white);
  }
  .brand-name {
    font-family: "Arimo", Arial, sans-serif;
    font-weight: 700; font-size: 40px; line-height: 1.05;
    color: var(--white);
    text-transform: uppercase;
  }
  .service-panel {
    position: absolute; right: 0; top: 400px;
    width: 250px; height: 410px;
    background: linear-gradient(180deg, rgba(223,227,231,.92), var(--panel-grey));
  }
  .thumb {
    position: absolute; left: 20px;
    width: 212px; height: 124px;
    border: 6px solid var(--white);
    box-shadow: 0 2px 6px rgba(0,0,0,.25);
  }
  .thumb--cleaner { top: 12px; background: linear-gradient(135deg, #8fc4ea, #2e78c0); }
  .thumb--hose { top: 146px; background: linear-gradient(135deg, #5fa6e0, #1d5ea6); }
  .thumb--technician { top: 280px; background: linear-gradient(135deg, #7fb48a, #5ea0d0); }
  .offer-banner {
    position: absolute; left: 20px; top: 420px;
    width: 330px; padding: 16px 18px 18px;
    border-radius: 10px;
    background: linear-gradient(180deg, var(--navy), var(--navy-dark));
    color: var(--white);
    box-shadow: 0 3px 8px rgba(0,0,0,.3);
  }
  .offer-title {
    font-family: "Bangers", "Impact", sans-serif;
    font-weight: 400;
    font-size: 42px; letter-spacing: 1px; line-height: 1;
  }
  .offer-price { color: var(--pool-light); }
  .offer-details { margin-top: 10px; font-size: 16px; line-height: 1.3; }
  .info {
    position: absolute; left: 24px; top: 610px; width: 320px;
    color: var(--text-dark);
  }
  .info-heading {
    font-weight: 700; font-size: 22px; color: var(--accent-blue);
    text-transform: uppercase;
  }
  .info-text { font-size: 15px; line-height: 1.35; margin: 4px 0 18px; }
  .contact-band {
    position: absolute; left: 0; bottom: 0;
    width: 600px; height: 90px;
    background: var(--band-blue);
    color: var(--white);
    display: flex; align-items: center; justify-content: space-between;
    padding: 0 26px;
    font-weight: 700; font-size: 21px;
  }
  .contact-item { display: flex; align-items: center; gap: 10px; }
  .contact-item svg { width: 22px; height: 22px; fill: var(--white); }
</style>
</head>
<body>
  <main class="flyer">
    <div class="hero-photo" role="img" aria-label="Woman relaxing at the stone edge of a blue pool, splashing water toward a waterfall"></div>

    <div class="brand">
      <span class="brand-dot"></span>
      <span class="brand-name">Bluecrest<br>Pool Services</span>
    </div>

    <aside class="service-panel">
      <div class="thumb thumb--cleaner" role="img" aria-label="Automatic pool cleaner being lifted from the water"></div>
      <div class="thumb thumb--hose" role="img" aria-label="Hand holding a vacuum hose under the water"></div>
      <div class="thumb thumb--technician" role="img" aria-label="Technician servicing equipment beside a pool"></div>
    </aside>

    <section class="offer-banner">
      <h1 class="offer-title">Service Call <span class="offer-price">$45</span></h1>
      <p class="offer-details">which Includes: Chemical Balance, Inspect all equipment, Skim water surface, clean filters.</p>
    </section>

    <section class="info">
      <h2 class="info-heading">Vacuum $10</h2>
      <p class="info-text">Please Call, txt or Email for chemical price list</p>
      <h2 class="info-heading">Other Services Include:</h2>
      <p class="info-text">Supply and install Pumps, Chlorinators, Automatic Cleaners &amp; Spare Parts</p>
    </section>

    <footer class="contact-band">
      <span class="contact-item">
        <svg viewBox="0 0 24 24" aria-hidden="true"><path d="M6.6 10.8a15.1 15.1 0 0 0 6.6 6.6l2.2-2.2a1 1 0 0 1 1-.25 11.4 11.4 0 0 0 3.6.57 1 1 0 0 1 1 1V20a1 1 0 0 1-1 1A17 17 0 0 1 3 4a1 1 0 0 1 1-1h3.5a1 1 0 0 1 1 1c0 1.25.2 2.45.57 3.57a1 1 0 0 1-.25 1z"/></svg>
        0417283951
      </span>
      <span class="contact-item">
        <svg viewBox="0 0 24 24" aria-hidden="true"><path d="M2 5h20v14H2zm2 2v.5l8 5 8-5V7zm0 2.9V17h16V9.9l-8 5z"/></svg>
        TideDesk@quellmail.com
      </span>
    </footer>
  </main>
</body>
</html>
```